New Boutique Pilates and Barre studio needs a flyer to promote classes.

Our studio is called 'The Willow Loft'. We are a boutique studio in Sydney that offers pilates mat and Barre classes with a maximum of 8 participants.

We need a flyer to promote our new studio that is opening mid-January 2015. Our goal is to motivate clients to cherish and nurture their bodies by participating in either our Pilates mat classes and/or our barre classes.

The flyer needs to communicate high-end, boutique classes that welcome those aged from 17-70 who would like achieve a stronger, leaner and dancer-like physique.

We would like our logo and a picture on the front with our contact details . The front should also say "First class is free!" (somewhere down the bottom).

A description of our classes as well as a map of our location should be on the back. Please see attached word document for copy.
I have attached our logo and contact details as well as pictures that may be used.

Please keep it uncluttered and elegant.
Updates

I have added a few pilates photos and a few requirements for the front of the flyer. Thanks

Industry/Entity Type

Boutique

Requirements
Must have

• MUST INCLUDE ON THE FRONT:
Please make sure my logo is very clear.

* Barre Classes
* Pilates Mat Classes
Private Studio in Castle Hill, Sydney
'First Class is free!'
Contact details: (Phone, website, email and address)

```html
<!DOCTYPE html>
<html lang="en">
<head>
<meta charset="utf-8">
<title>The Willow Loft – Studio Flyer</title>
<link href="https://fonts.googleapis.com/css2?family=Arimo:ital,wght@0,400;0,700;1,700&family=Oswald:wght@500;600&display=swap" rel="stylesheet">
<style>
  :root {
    --backdrop: #e9e6e1;
    --paper: #ffffff;
    --brand-blue: #1f4f9e;
    --band-blue: #1d3f82;
    --night: #232326;
    --gold: #e8b23a;
    --ink: #333333;
    --muted: #8a8a8a;
    --badge-red: #c0161c;
    --leaf-light: #d9e7a6;
    --leaf-mid: #86a94a;
    --leaf-dark: #3c5a22;
    --autumn: #b88a3c;
    --studio-light: #f3f1ee;
    --studio-warm: #d9c3ad;
  }
  * { box-sizing: border-box; margin: 0; padding: 0; }
  html, body { width: 1200px; height: 800px; overflow: hidden; }
  body {
    background: var(--backdrop);
    font-family: "Arimo", Arial, sans-serif;
    color: var(--ink);
    position: relative;
  }
  .sheet {
    position: absolute;
    top: 40px;
    width: 510px;
    height: 720px;
    background: var(--paper);
    overflow: hidden;
    box-shadow: 0 6px 18px rgba(0,0,0,.18);
  }
  .sheet--front { left: 60px; }
  .sheet--back { left: 630px; }

  /* Front */
  .hero-photo {
    position: absolute; inset: 0 0 175px 0;
    background:
      radial-gradient(ellipse 40% 55% at 55% 45%, rgba(40,40,48,.55), transparent 70%),
      linear-gradient(180deg, var(--leaf-light) 0%, var(--leaf-mid) 40%, var(--leaf-dark) 70%, var(--autumn) 100%);
  }
  .wordmark {
    font-family: "Arimo", Arial, sans-serif;
    font-weight: 700;
    color: var(--brand-blue);
    display: flex; align-items: center; gap: 10px;
    white-space: nowrap;
  }
  .wordmark__dot {
    width: 14px; height: 14px; border-radius: 50%;
    background: var(--brand-blue);
  }
  .sheet--front .wordmark {
    position: absolute; top: 70px; left: 40px; font-size: 38px;
  }
  .class-band {
    position: absolute; left: 0; right: 0; top: 545px; height: 40px;
    background: var(--band-blue);
    color: #fff;
    font-size: 12.5px; font-weight: 700;
    display: flex; align-items: center; padding-left: 20px; gap: 12px;
    white-space: nowrap;
  }
  .free-badge {
    position: absolute; right: 26px; top: 446px;
    width: 92px; height: 92px; border-radius: 50%;
    background: radial-gradient(circle at 40% 35%, #e23a3f, var(--badge-red) 60%, #8c0d12);
    border: 3px solid #fff;
    color: #fff; text-align: center;
    display: flex; flex-direction: column; justify-content: center;
    transform: rotate(-18deg);
    box-shadow: 0 3px 8px rgba(0,0,0,.35);
  }
  .free-badge__small { font-size: 10px; font-weight: 700; letter-spacing: .5px; }
  .free-badge__big { font-family: "Oswald", sans-serif; font-size: 26px; font-weight: 600; line-height: 1; }
  .contact-block {
    position: absolute; left: 0; right: 0; bottom: 0; height: 135px;
    background: var(--night);
    display: flex; align-items: center; padding: 0 20px;
  }
  .contact-block__call {
    font-family: "Oswald", sans-serif; font-weight: 600;
    color: var(--gold); font-size: 27px; white-space: nowrap; margin-right: 14px;
  }
  .contact-block__arrow { width: 18px; height: 50px; margin-right: 14px; flex-shrink: 0; }
  .contact-list {
    list-style: none; color: #d8d8d8; font-size: 11.5px;
    border-left: 1px solid #555; padding-left: 12px; white-space: nowrap;
  }
  .contact-list li { display: flex; align-items: center; gap: 7px; margin: 4px 0; }
  .contact-list .phone { color: var(--gold); font-size: 16px; font-weight: 700; }
  .contact-icon { width: 14px; height: 14px; background: #555; border-radius: 2px; display: flex; align-items: center; justify-content: center; flex-shrink: 0; }

  /* Back */
  .sheet--back .wordmark {
    position: absolute; top: 52px; left: 0; right: 0; justify-content: center; font-size: 34px;
  }
  .studio-photo {
    position: absolute; left: 0; right: 0; top: 300px; height: 305px;
    background:
      linear-gradient(180deg, var(--paper) 0%, rgba(255,255,255,0) 35%),
      linear-gradient(90deg, var(--studio-light) 0%, var(--studio-warm) 45%, #c9a889 70%, var(--studio-light) 100%);
  }
  .copy {
    position: absolute; top: 135px; left: 26px; right: 26px;
    font-size: 10.5px; line-height: 1.4;
  }
  .copy p { margin-bottom: 8px; }
  .copy h2 {
    font-family: "Oswald", sans-serif; font-weight: 500;
    color: var(--brand-blue); font-size: 17px; margin: 12px 0 2px;
  }
  .copy .lead { font-weight: 700; font-style: italic; }
  .benefit-band {
    position: absolute; left: 0; right: 0; top: 605px; height: 34px;
    background: var(--band-blue); color: #fff; text-align: center;
    font-size: 9.5px; padding-top: 4px;
  }
  .benefit-band strong { display: block; font-size: 10px; margin-top: 2px; }
  .closing {
    position: absolute; left: 0; right: 0; bottom: 0; height: 81px;
    background: var(--night);
    font-family: "Oswald", sans-serif; font-weight: 500;
    color: var(--gold); text-align: center; font-size: 17px; line-height: 1.3;
    padding-top: 14px;
  }
</style>
</head>
<body>

<section class="sheet sheet--front">
  <div class="hero-photo" role="img" aria-label="Photo of a dancer in a black dress posing among sunlit trees and autumn leaves"></div>
  <div class="wordmark"><span class="wordmark__dot"></span>The Willow Loft</div>
  <div class="class-band">
    <span>• Barre Classes</span>
    <span>• Pilates Mat Classes Private Studio in Castle Hill, Sydney</span>
  </div>
  <div class="free-badge">
    <span class="free-badge__small">FIRST CLASS IS</span>
    <span class="free-badge__big">FREE!</span>
  </div>
  <div class="contact-block">
    <div class="contact-block__call">Contact Us Today!</div>
    <svg class="contact-block__arrow" viewBox="0 0 22 60" aria-hidden="true"><polygon points="2,2 20,30 2,58" fill="#55555a"/></svg>
    <ul class="contact-list">
      <li class="phone"><span class="contact-icon"><svg width="9" height="9" viewBox="0 0 10 10"><path d="M2 1l2 2-1 1.5c.7 1.3 1.2 1.8 2.5 2.5L7 6l2 2-1.5 1.5C4.5 9 1 5.5.5 2.5z" fill="#ddd"/></svg></span>0400 318 562</li>
      <li><span class="contact-icon"><svg width="9" height="9" viewBox="0 0 10 10"><rect x="1" y="2" width="8" height="6" fill="none" stroke="#ddd"/><path d="M1 2l4 3 4-3" fill="none" stroke="#ddd"/></svg></span>info@thewillowloft.com.au</li>
      <li><span class="contact-icon"><svg width="9" height="9" viewBox="0 0 10 10"><circle cx="5" cy="5" r="4" fill="none" stroke="#ddd"/><path d="M1 5h8M5 1v8" stroke="#ddd"/></svg></span>www.thewillowloft.com.au</li>
      <li><span class="contact-icon"><svg width="9" height="9" viewBox="0 0 10 10"><path d="M5 9L2 5a3 3 0 1 1 6 0z" fill="#ddd"/></svg></span>24 Fernleigh Street, Castle Hill NSW 2154</li>
    </ul>
  </div>
</section>

<section class="sheet sheet--back">
  <div class="studio-photo" role="img" aria-label="Photo of women stretching their arms overhead at a ballet barre in a bright studio"></div>
  <div class="wordmark"><span class="wordmark__dot"></span>The Willow Loft</div>
  <div class="copy">
    <p>The Willow Loft is a boutique studio in Castle Hill, Sydney. We offer Pilates mat and barre classes for adults of any age, who are seeking a stronger, leaner dancer-like physique.</p>
    <h2>Barre classes:</h2>
    <p>Our Barre classes are a 50 minute fusion of Pilates, dance and total body strengthening through the use of the ballet barre, light hand weights, pilates balls and body weight.</p>
    <p>We move to the latest upbeat pop style music, making it fun and easy to forget that you are working out! Best of all, you do not need to be a dancer or have any kind of dance experience to join in. If you love moving to music then this class is just right for you.</p>
    <h2>Pilates Mat classes:</h2>
    <p class="lead">Pilates is a body-conditioning program designed to teach efficient movement patterns and provide general well-being using controlled exercises and deliberate breathing patterns.</p>
    <p>Our Pilates mat classes consist of a 50 minute routine based on classical matwork exercises that include props such as therabands, balls, foam rollers, light weights and a barre to challenge balance and lower body strength and stability.</p>
  </div>
  <div class="benefit-band">
    Pilates offers benefits such as improvement in:
    <strong>Strength • Body tone • Flexibility • Posture • Efficient movement and • Mind/Body connection.</strong>
  </div>
  <div class="closing">All of our classes have a maximum of 8 participants,<br>so reserve your space today!</div>
</section>

</body>
</html>
```